An our door sign really promoting our clinic and services

We have a new sports medicine clinic called ASHBRAE SPORTS MEDICINE.
We want to make a really nice external sign at our clinic using a photo of our team we really like. I have attached the photo.
We want to simply include our LOGO and also signs with these slogan options. So we want different signs with these different slogans so we can choose what we really like.
This should be a simple and quite design.

The SLOGANS WE WOULD LIKE TO SEE ON THE SIGN (only one slogan per sign in the drafts)

1. Your Journey. Our Expertise
2. Where better health begins
3. Building the best version of you
4. Your health, in expert hands
5. Reaching new heights in your health
6. Your path to peak performance starts here

I have also included different versions of our logo based on the background and how you set the sign up

So summary
1. Image attached
2. Slogan options we would like to see them all
3. Logo attached (various options based on how you set the background up)
4. Size of sign is 2935mm wide x 1885mm high

```html
<!DOCTYPE html>
<html lang="en">
<head>
<meta charset="utf-8">
<title>Ashbrae Sports Medicine – Exterior Sign Concepts</title>
<link href="https://fonts.googleapis.com/css2?family=Unbounded:wght@600;700&display=swap" rel="stylesheet">
<style>
  :root{
    --navy:#141a4e;
    --cyan:#3fc1ec;
    --white:#ffffff;
    --board:#e6e6e7;
    --photo-a:#6d6a66;
    --photo-b:#c9c4bb;
  }
  html,body{margin:0;padding:0;overflow:hidden}
  body{width:1200px;height:839px;background:radial-gradient(ellipse at center,#f1f1f2 0%,var(--board) 100%);position:relative;font-family:"Unbounded",sans-serif}
  .sign{position:absolute;width:519px;height:334px;box-shadow:0 14px 18px -12px rgba(0,0,0,.35)}
  .sign svg{display:block;width:100%;height:100%}
  .sign--journey{left:59px;top:58px}
  .sign--heights{left:618px;top:58px}
  .sign--begins{left:59px;top:442px}
  .sign--best{left:618px;top:442px}
  .headline{font-family:"Unbounded",sans-serif;font-weight:700;font-size:36px;letter-spacing:-0.5px}
  .brand{font-family:"Unbounded",sans-serif;font-weight:600}
  .fill-navy{fill:var(--navy)}
  .fill-cyan{fill:var(--cyan)}
  .fill-white{fill:var(--white)}
</style>
</head>
<body>
<svg width="0" height="0" style="position:absolute">
  <defs>
    <linearGradient id="photoTone" x1="0" y1="0" x2="1" y2="1">
      <stop offset="0" stop-color="#b9b3a8"/>
      <stop offset=".5" stop-color="#5f5c5a"/>
      <stop offset="1" stop-color="#2f3b34"/>
    </linearGradient>
    <linearGradient id="cyanFade" x1="0" y1="0" x2="1" y2="1">
      <stop offset="0" stop-color="#3fc1ec" stop-opacity=".95"/>
      <stop offset="1" stop-color="#3fc1ec" stop-opacity=".15"/>
    </linearGradient>
    <linearGradient id="whiteFade" x1="0" y1="0" x2="1" y2="0">
      <stop offset="0" stop-color="#ffffff" stop-opacity="0"/>
      <stop offset=".35" stop-color="#ffffff" stop-opacity="1"/>
    </linearGradient>
  </defs>
</svg>

<!-- Sign 1 -->
<div class="sign sign--journey">
  <svg viewBox="0 0 648 417">
    <rect class="fill-navy" width="648" height="417"/>
    <polygon points="236,0 648,0 648,417 410,417" fill="url(#photoTone)" role="img" aria-label="Team photo: two clinicians reviewing a tablet in the gym"/>
    <polygon class="fill-cyan" points="222,0 236,0 410,417 396,417"/>
    <polygon class="fill-navy" points="546,0 556,0 648,212 648,232"/>
    <polygon class="fill-cyan" points="556,0 648,0 648,212"/>
    <g class="brand fill-white">
      <circle class="fill-cyan" cx="36" cy="50" r="7"/>
      <text x="50" y="55" font-size="15">ASHBRAE</text>
      <text x="50" y="66" font-size="7" letter-spacing="2.2">SPORTS MEDICINE</text>
    </g>
    <text class="headline" x="24">
      <tspan x="24" y="262" class="fill-cyan">YOUR</tspan>
      <tspan x="24" y="300" class="fill-cyan">JOURNEY.</tspan>
      <tspan x="24" y="338" class="fill-white">OUR</tspan>
      <tspan x="24" y="376" class="fill-white">EXPERTISE</tspan>
    </text>
  </svg>
</div>

<!-- Sign 2 -->
<div class="sign sign--heights">
  <svg viewBox="0 0 648 417">
    <rect class="fill-navy" width="648" height="417"/>
    <path d="M0 0H648V100C500 195 300 232 0 238Z" fill="url(#photoTone)" role="img" aria-label="Team photo: two clinicians reviewing a tablet in the gym"/>
    <path d="M300 0H648V100C560 165 470 205 390 215C340 190 305 110 300 0Z" fill="url(#whiteFade)"/>
    <path class="fill-cyan" d="M648 100V122C500 215 300 242 0 242V238C300 232 500 195 648 100Z"/>
    <g class="brand fill-navy">
      <circle class="fill-cyan" cx="378" cy="86" r="9"/>
      <text x="394" y="92" font-size="21">ASHBRAE</text>
      <text x="394" y="105" font-size="8.5" letter-spacing="3" class="fill-cyan">SPORTS MEDICINE</text>
    </g>
    <text class="headline" text-anchor="middle">
      <tspan x="324" y="302"><tspan class="fill-cyan">REACHING</tspan><tspan class="fill-white"> NEW</tspan></tspan>
      <tspan x="324" y="340"><tspan class="fill-white">HEIGHTS</tspan><tspan class="fill-cyan"> IN YOUR</tspan></tspan>
      <tspan x="324" y="378" class="fill-cyan">HEALTH...</tspan>
    </text>
  </svg>
</div>

<!-- Sign 3 -->
<div class="sign sign--begins">
  <svg viewBox="0 0 648 417">
    <rect class="fill-navy" width="648" height="417"/>
    <polygon points="236,0 648,0 648,417 410,417" fill="url(#photoTone)" role="img" aria-label="Team photo: two clinicians reviewing a tablet in the gym"/>
    <polygon points="236,0 450,0 330,225" fill="url(#cyanFade)"/>
    <polygon class="fill-white" points="222,0 236,0 410,417 396,417"/>
    <g class="brand fill-white">
      <circle class="fill-cyan" cx="36" cy="50" r="7"/>
      <text x="50" y="55" font-size="15">ASHBRAE</text>
      <text x="50" y="66" font-size="7" letter-spacing="2.2">SPORTS MEDICINE</text>
    </g>
    <text class="headline">
      <tspan x="24" y="262" class="fill-cyan">WHERE</tspan>
      <tspan x="48" y="300" class="fill-white">BETTER</tspan>
      <tspan x="24" y="338" class="fill-cyan">HEALTH</tspan>
      <tspan x="48" y="376" class="fill-white">BEGINS...</tspan>
    </text>
  </svg>
</div>

<!-- Sign 4 -->
<div class="sign sign--best">
  <svg viewBox="0 0 648 417">
    <rect width="648" height="417" fill="url(#photoTone)" role="img" aria-label="Team photo: two clinicians reviewing a tablet in the gym"/>
    <path class="fill-navy" d="M0 0H404C385 120 260 238 0 232Z"/>
    <path class="fill-white" d="M0 0H396C376 115 255 225 0 218Z"/>
    <path class="fill-cyan" d="M395 417C470 360 560 325 648 318V330C565 337 480 370 420 417Z"/>
    <path class="fill-navy" d="M420 417C480 370 565 337 648 330V417Z"/>
    <g class="brand fill-white">
      <circle class="fill-cyan" cx="521" cy="379" r="5"/>
      <text x="530" y="382" font-size="10">ASHBRAE</text>
      <text x="530" y="390" font-size="5" letter-spacing="1.5">SPORTS MEDICINE</text>
    </g>
    <text class="headline">
      <tspan x="32" y="64" class="fill-navy">BUILDING</tspan>
      <tspan x="32" y="102" class="fill-cyan">THE BEST</tspan>
      <tspan x="32" y="140" class="fill-navy">VERSION</tspan>
      <tspan x="32" y="178" class="fill-cyan">OF YOU</tspan>
    </text>
  </svg>
</div>
</body>
</html>
```